CopperWren Works, LLC Corporate Web Site

The goal of this web site is simple. To provide an information and corporate information site for people who click on company links from other web sites. Put simply, this web site is primarily a brochure web site for the parent business. It will contain information about the company and our products with links to those products. It will be designed as a small web site but scalable as we add more products and services to our repertoire.

Please see the PDF in the uploaded files/media for more information on colors and basic guidelines, but be creative for sure.

Target Market(s)

General

Industry/Entity Type

Technology, Software

Coding

Coded - Design and coding required

Font styles to use
Other font styles liked:
• Goliath, Roboto

Colors
FFC000
F8CF3A
FAE287
FDF2CF
FEFAEE

Requirements
Must have
• Home page template, interior template, News/Press release template
Nice to have
• Searchable
Should not have
• carousels, one-page design

```html
<!DOCTYPE html>
<html lang="en">
<head>
<meta charset="utf-8">
<title>CopperWren Works, LLC – About Us</title>
<link rel="stylesheet" href="https://fonts.googleapis.com/css2?family=Baloo+2:wght@700;800&family=Roboto:wght@400;500;700&display=swap">
<style>
:root{
  --orange:#F7A21B;
  --orange-deep:#F28C0F;
  --purple:#5F63A9;
  --ink:#141414;
  --footer:#0E0E10;
  --text:#6B6B6B;
  --line:#E2E2E2;
  --page:#F3F3F3;
  --white:#FFFFFF;
  --photo-a:#1B2A44;
  --photo-b:#3E5A80;
  --photo-c:#8A9BB3;
}
*{box-sizing:border-box;margin:0;padding:0}
html,body{width:1200px;height:2376px;overflow:hidden;background:var(--page);font-family:'Roboto',Arial,sans-serif;color:var(--text)}
.board{position:relative;width:1200px;height:2376px}
.screen{position:absolute;background:var(--white);overflow:hidden;border:1px solid var(--line);border-radius:10px;box-shadow:0 2px 10px rgba(0,0,0,.08)}
.abs{position:absolute}
.brand{font-family:'Baloo 2',sans-serif;font-weight:800;color:var(--orange);letter-spacing:.5px;line-height:1;display:flex;align-items:center;gap:6px}
.brand::before{content:"";width:.55em;height:.55em;border-radius:50%;background:var(--orange)}
.nav{position:absolute;left:0;top:0;width:100%;background:var(--white);display:flex;align-items:center;justify-content:space-between}
.nav-links{display:flex;gap:14px;font-size:8.5px;color:var(--ink);align-items:center}
.nav-links .active{color:var(--orange)}
.search-dot{width:14px;height:14px;border-radius:50%;border:1.5px solid var(--purple)}
.burger{width:14px;height:10px;border-top:2px solid var(--ink);border-bottom:2px solid var(--ink);position:relative}
.burger::after{content:"";position:absolute;left:0;right:0;top:2px;border-top:2px solid var(--ink)}
.photo{background:linear-gradient(135deg,var(--photo-a),var(--photo-b) 55%,var(--photo-c))}
.photo.warm{background:linear-gradient(135deg,#3A3F52,#7C8396 50%,#C8C3BA)}
.photo.blue{background:linear-gradient(135deg,#0F2450,#2A5FA8 55%,#7FB2E0)}
.photo.night{background:linear-gradient(135deg,#0A0E22,#26306A 55%,#5A4A8C)}
.heading{font-family:'Baloo 2',sans-serif;font-weight:800;color:var(--orange);text-transform:uppercase;line-height:1}
.copy{font-size:8.5px;line-height:1.55;color:var(--text)}
.btn{position:absolute;background:var(--purple);color:var(--white);font-size:8px;font-weight:500;padding:5px 14px;border-radius:2px}
.btn.light{background:var(--white);color:var(--purple)}
.band{position:absolute;left:0;width:100%;background:var(--purple);color:var(--white)}
.band .copy{color:#E7E8F5;text-align:center}
.sub{color:var(--purple);font-weight:700;line-height:1.3}
.list{list-style:none;font-size:8.5px;line-height:1.9;color:var(--text)}
.list li::before{content:"";display:inline-block;width:4px;height:4px;border-radius:50%;background:var(--orange);margin-right:6px;vertical-align:middle}
.footer{position:absolute;left:0;width:100%;color:#BDBDBD}
.foot-cols{display:grid;grid-template-columns:repeat(4,1fr);gap:22px}
.foot-cols h4{color:var(--orange);font-size:9px;font-weight:700;margin-bottom:8px;text-transform:uppercase}
.foot-cols p{font-size:8px;line-height:1.9}
.field{height:16px;background:#2A2A2E;border-radius:2px;margin:6px 0}
.bottom-bar{position:absolute;left:0;width:100%;background:var(--orange);color:var(--ink);font-size:7.5px;display:flex;align-items:center;justify-content:space-between;padding:0 20px}
.dots{display:flex;gap:6px}
.dots span{width:9px;height:9px;border-radius:50%;background:var(--ink)}
svg.shape{position:absolute;left:0;display:block}
</style>
</head>
<body>
<div class="board">

<!-- Desktop hero preview -->
<section class="screen" style="left:32px;top:48px;width:868px;height:520px">
  <header class="nav" style="height:44px;padding:0 24px">
    <div class="brand" style="font-size:20px">CopperWren</div>
    <nav class="nav-links"><span>Home</span><span class="active">About</span><span>Products</span><span>Projects</span><span>Contributors</span><span>News</span><span>Contact</span><span class="search-dot"></span></nav>
  </header>
  <svg class="shape" style="top:44px" width="868" height="296" viewBox="0 0 868 296" preserveAspectRatio="none">
    <polygon points="0,210 434,296 868,210 868,226 434,296 0,226" fill="var(--orange)"/>
    <polygon points="0,0 868,0 868,206 434,286 0,206" fill="var(--ink)"/>
  </svg>
  <div class="abs photo" role="img" aria-label="Businessman working at a laptop in a modern office" style="left:0;top:44px;width:868px;height:286px;clip-path:polygon(0 0,100% 0,100% 72%,50% 100%,0 72%)"></div>
  <h1 class="heading abs" style="left:24px;top:366px;font-size:28px">About Us</h1>
  <p class="copy abs" style="left:24px;top:404px;width:400px">Lorem Ipsum is simply dummy text of the printing and typesetting industry. Lorem Ipsum has been the industry's standard dummy text ever since the 1500s, when an unknown printer took a galley of type and scrambled it to make a type specimen book. It has survived not only five centuries.</p>
  <div class="abs photo warm" role="img" aria-label="Team meeting around a table" style="left:520px;top:380px;width:260px;height:140px"></div>
</section>

<!-- Mobile hero preview -->
<section class="screen" style="left:960px;top:48px;width:208px;height:512px">
  <header class="nav" style="height:32px;padding:0 10px">
    <div class="brand" style="font-size:13px">CopperWren</div>
    <div class="burger"></div>
  </header>
  <svg class="shape" style="top:32px" width="208" height="126" viewBox="0 0 208 126" preserveAspectRatio="none">
    <polygon points="0,92 104,126 208,92 208,100 104,126 0,100" fill="var(--orange)"/>
  </svg>
  <div class="abs photo" role="img" aria-label="Businessman working at a laptop" style="left:0;top:32px;width:208px;height:118px;clip-path:polygon(0 0,100% 0,100% 75%,50% 100%,0 75%)"></div>
  <h1 class="heading abs" style="left:12px;top:170px;font-size:18px">About Us</h1>
  <p class="copy abs" style="left:12px;top:196px;width:184px;font-size:7px">Lorem Ipsum is simply dummy text of the printing and typesetting industry. Lorem Ipsum has been the industry's standard dummy text ever since the 1500s, when an unknown printer took a galley of type and scrambled it to make a type specimen book.</p>
  <div class="abs photo warm" role="img" aria-label="Team meeting around a table" style="left:12px;top:282px;width:184px;height:96px"></div>
  <span class="btn" style="left:74px;top:396px">Read More</span>
  <div class="band" style="top:432px;height:80px">
    <p class="copy abs" style="left:12px;top:16px;width:184px;font-size:7px">Lorem Ipsum is simply dummy text of the printing and typesetting industry. Lorem Ipsum has been the industry's standard dummy text.</p>
  </div>
</section>

<!-- Desktop full page -->
<section class="screen" style="left:32px;top:600px;width:868px;height:1720px">
  <header class="nav" style="height:44px;padding:0 24px">
    <div class="brand" style="font-size:20px">CopperWren</div>
    <nav class="nav-links"><span>Home</span><span class="active">About</span><span>Products</span><span>Projects</span><span>Contributors</span><span>News</span><span>Contact</span></nav>
  </header>
  <svg class="shape" style="top:44px" width="868" height="212" viewBox="0 0 868 212" preserveAspectRatio="none">
    <polygon points="0,146 434,212 868,146 868,160 434,212 0,160" fill="var(--orange)"/>
  </svg>
  <div class="abs photo" role="img" aria-label="Businessman working at a laptop in a modern office" style="left:0;top:44px;width:868px;height:200px;clip-path:polygon(0 0,100% 0,100% 70%,50% 100%,0 70%)"></div>

  <h2 class="heading abs" style="left:24px;top:272px;font-size:28px">About Us</h2>
  <p class="copy abs" style="left:24px;top:312px;width:400px">Lorem Ipsum is simply dummy text of the printing and typesetting industry. Lorem Ipsum has been the industry's standard dummy text ever since the 1500s, when an unknown printer took a galley of type and scrambled it to make a type specimen book. It has survived not only five centuries, but also the leap into electronic typesetting, remaining essentially unchanged. It was popularised in the 1960s with the release of sheets containing passages.</p>
  <span class="btn" style="left:24px;top:410px">Read More</span>
  <div class="abs photo warm" role="img" aria-label="Colleagues collaborating at a desk" style="left:500px;top:292px;width:290px;height:150px"></div>

  <div class="band" style="top:468px;height:180px">
    <p class="copy abs" style="left:134px;top:40px;width:600px">Lorem Ipsum is simply dummy text of the printing and typesetting industry. Lorem Ipsum has been the industry's standard dummy text ever since the 1500s, when an unknown printer took a galley of type and scrambled it to make a type specimen book.</p>
    <p class="copy abs" style="left:134px;top:84px;width:600px">It has survived not only five centuries, but also the leap into electronic typesetting, remaining essentially unchanged. It was popularised in the 1960s with the release of sheets containing passages, and more recently with desktop publishing software.</p>
    <span class="btn light" style="left:404px;top:136px">Read More</span>
  </div>

  <div class="abs photo blue" role="img" aria-label="Hand touching a glowing digital interface" style="left:40px;top:724px;width:300px;height:210px"></div>
  <h2 class="heading abs" style="left:390px;top:754px;font-size:26px">Title Here</h2>
  <p class="copy abs" style="left:390px;top:790px;width:400px">Lorem Ipsum is simply dummy text of the printing and typesetting industry. Lorem Ipsum has been the industry's standard dummy text ever since the 1500s, when an unknown printer took a galley of type and scrambled it to make a type specimen book. It has survived not only five centuries, but also the leap into electronic typesetting.</p>
  <span class="btn" style="left:390px;top:870px">Read More</span>

  <h2 class="heading abs" style="left:40px;top:1006px;font-size:26px">Title Here</h2>
  <p class="sub abs" style="left:40px;top:1040px;width:360px;font-size:13px">Lorem Ipsum is simply dummy text of the printing and typesetting industry</p>
  <ul class="list abs" style="left:40px;top:1084px;width:380px">
    <li>Sed ut perspiciatis unde omnis iste natus error</li>
    <li>Nemo enim ipsam voluptatem quia voluptas sit</li>
    <li>Neque porro quisquam est qui dolorem ipsum</li>
    <li>Ut enim ad minima veniam quis nostrum</li>
    <li>Quis autem vel eum iure reprehenderit qui</li>
    <li>At vero eos et accusamus et iusto odio</li>
  </ul>
  <div class="abs photo night" role="img" aria-label="Developer coding at a monitor at night" style="left:480px;top:1020px;width:300px;height:190px"></div>

  <svg class="shape" style="top:1330px" width="868" height="390" viewBox="0 0 868 390" preserveAspectRatio="none">
    <polygon points="0,60 434,0 868,60 868,390 0,390" fill="var(--orange)"/>
    <polygon points="0,72 434,14 868,72 868,390 0,390" fill="var(--footer)"/>
  </svg>
  <div class="footer" style="top:1330px;height:390px">
    <div class="brand abs" style="left:364px;top:58px;font-size:24px">CopperWren</div>
    <div class="foot-cols abs" style="left:40px;top:120px;width:788px">
      <div><h4>Contact Info</h4><p>42 Lantern Row, Suite 8<br>Brookvale, OR 97000<br>(555) 010-2468<br>hello@copperwrenworks.example</p></div>
      <div><h4>Quick Link</h4><p>Home<br>About<br>Products<br>Projects<br>News</p></div>
      <div><h4>Services</h4><p>Software Design<br>Web Apps<br>Digital Consulting<br>Cloud Hosting<br>Support Plans</p></div>
      <div><h4>Newsletter</h4><p>Subscribe for the latest updates.</p><div class="field"></div><span class="btn" style="position:static;display:inline-block">Subscribe</span></div>
    </div>
    <div class="bottom-bar" style="top:360px;height:30px"><span>© 2024 CopperWren Works, LLC. All rights reserved.</span><div class="dots"><span></span><span></span><span></span><span></span></div></div>
  </div>
</section>

<!-- Mobile full page -->
<section class="screen" style="left:960px;top:600px;width:208px;height:1420px">
  <header class="nav" style="height:32px;padding:0 10px">
    <div class="brand" style="font-size:13px">CopperWren</div>
    <div class="burger"></div>
  </header>
  <svg class="shape" style="top:32px" width="208" height="116" viewBox="0 0 208 116" preserveAspectRatio="none">
    <polygon points="0,84 104,116 208,84 208,92 104,116 0,92" fill="var(--orange)"/>
  </svg>
  <div class="abs photo" role="img" aria-label="Businessman working at a laptop" style="left:0;top:32px;width:208px;height:108px;clip-path:polygon(0 0,100% 0,100% 75%,50% 100%,0 75%)"></div>
  <h2 class="heading abs" style="left:12px;top:164px;font-size:18px">About Us</h2>
  <p class="copy abs" style="left:12px;top:190px;width:184px;font-size:7px">Lorem Ipsum is simply dummy text of the printing and typesetting industry. Lorem Ipsum has been the industry's standard dummy text ever since the 1500s, when an unknown printer took a galley of type.</p>
  <div class="abs photo warm" role="img" aria-label="Colleagues collaborating at a desk" style="left:12px;top:262px;width:184px;height:86px"></div>
  <span class="btn" style="left:74px;top:360px">Read More</span>

  <div class="band" style="top:392px;height:210px">
    <h2 class="heading abs" style="left:12px;top:18px;font-size:16px">Title Here</h2>
    <p class="copy abs" style="left:12px;top:44px;width:184px;font-size:7px">Lorem Ipsum is simply dummy text of the printing and typesetting industry. Lorem Ipsum has been the industry's standard dummy text ever since the 1500s.</p>
    <p class="copy abs" style="left:12px;top:100px;width:184px;font-size:7px">It has survived not only five centuries, but also the leap into electronic typesetting, remaining essentially unchanged.</p>
    <span class="btn light" style="left:74px;top:168px">Read More</span>
  </div>

  <div class="abs photo blue" role="img" aria-label="Hand touching a glowing digital interface" style="left:12px;top:620px;width:184px;height:84px"></div>
  <h2 class="heading abs" style="left:12px;top:718px;font-size:16px">Title Here</h2>
  <p class="copy abs" style="left:12px;top:742px;width:184px;font-size:7px">Lorem Ipsum is simply dummy text of the printing and typesetting industry. Lorem Ipsum has been the industry's standard dummy text ever since the 1500s.</p>
  <span class="btn" style="left:74px;top:800px">Read More</span>

  <h2 class="heading abs" style="left:12px;top:836px;font-size:16px">Title Here</h2>
  <p class="sub abs" style="left:12px;top:858px;width:184px;font-size:9px">Lorem Ipsum is simply dummy text of the printing and typesetting industry</p>
  <ul class="list abs" style="left:12px;top:888px;width:184px;font-size:7px">
    <li>Sed ut perspiciatis unde omnis iste</li>
    <li>Nemo enim ipsam voluptatem quia</li>
    <li>Neque porro quisquam est qui</li>
    <li>Ut enim ad minima veniam quis</li>
  </ul>

  <svg class="shape" style="top:970px" width="208" height="450" viewBox="0 0 208 450" preserveAspectRatio="none">
    <polygon points="0,24 104,0 208,24 208,450 0,450" fill="var(--orange)"/>
    <polygon points="0,30 104,6 208,30 208,450 0,450" fill="var(--footer)"/>
  </svg>
  <div class="footer" style="top:970px;height:450px">
    <div class="brand abs" style="left:50px;top:40px;font-size:16px">CopperWren</div>
    <p class="abs" style="left:16px;top:74px;font-size:7px;line-height:2">42 Lantern Row, Suite 8<br>Brookvale, OR 97000<br>(555) 010-2468<br>hello@copperwrenworks.example</p>
    <div class="abs" style="left:16px;top:160px;width:176px;font-size:8px;color:var(--orange);font-weight:700;line-height:3.2;border-top:1px solid #2A2A2E">
      <div style="border-bottom:1px solid #2A2A2E">QUICK LINK</div>
      <div style="border-bottom:1px solid #2A2A2E">SERVICES</div>
      <div style="border-bottom:1px solid #2A2A2E">NEWSLETTER</div>
    </div>
    <div class="bottom-bar" style="top:400px;height:50px;flex-direction:column;justify-content:center;gap:6px;font-size:6.5px"><div class="dots"><span></span><span></span><span></span><span></span></div><span>© 2024 CopperWren Works, LLC.</span></div>
  </div>
</section>

</div>
</body>
</html>
```